Childcare Centre trifold brochure

Design a contemporary trifold brochure for a childcare centre that meets Australian printing requirements with supplied content, logo's, fonts and photo's. Please refer to the attached DL flyer front and back for similar possible style and content.

Target Market(s)

Families

Industry/Entity Type

Childcare

Requirements
Must have
• refer attached content, photo's, logo's and examples. Colours should be same as Pantone purple and green and or variations of. Refer attached dl flyer example.

```html
<!DOCTYPE html>
<html lang="en">
<head>
<meta charset="utf-8">
<title>Bright Sprouts – Trifold Brochure</title>
<link rel="stylesheet" href="https://fonts.googleapis.com/css2?family=Fredoka:wght@500;600&family=Nunito:wght@400;700;800&family=Schoolbell&display=swap">
<style>
:root{
  --purple:#8e2a8b;
  --purple-dark:#6e1f6c;
  --green:#56b447;
  --green-dark:#3f9a35;
  --blue:#2f9ad6;
  --ink:#4a4a4a;
  --paper:#ffffff;
  --stage:#dedede;
  --photo-warm:#b99a74;
  --photo-cool:#7a6c8f;
}
*{box-sizing:border-box;margin:0;padding:0}
html,body{width:1200px;height:2400px;overflow:hidden}
body{background:var(--stage);font-family:"Nunito",sans-serif;color:var(--ink);position:relative}
.spread{position:absolute;left:30px;width:1140px;height:806px;display:flex;box-shadow:0 10px 30px rgba(0,0,0,.18);background:var(--paper)}
.spread--outside{top:250px}
.spread--inside{top:1306px}
.panel{position:relative;width:380px;height:806px;overflow:hidden;background:var(--paper)}
.panel--wide{width:760px}
.abs{position:absolute}
.photo{position:absolute;left:0;width:100%}
.photo--warm{background:linear-gradient(160deg,#c9ab82,#8f7a5a 55%,#6d5f73)}
.photo--play{background:linear-gradient(135deg,#d9b9a0,#a46b8e 45%,#5a6a8a)}
.photo--yard{background:linear-gradient(180deg,#cfd6dc,#9a8a70 60%,#6f6150)}
.photo--child{background:linear-gradient(160deg,#a7b48e,#4d5c7a 55%,#2f3550)}
.curve{position:absolute;left:0;width:100%;display:block}
.handwrite{font-family:"Schoolbell",cursive;font-size:36px;line-height:1.05}
.body-copy{font-size:11.5px;line-height:1.5;margin-bottom:9px}
.pill{display:inline-block;background:var(--purple);color:#fff;font-family:"Fredoka",sans-serif;font-weight:600;font-size:20px;padding:4px 26px;border-radius:20px}
.pill--green{background:var(--green)}

/* flap panel */
.flap__intro{left:30px;top:34px;width:320px}
.flap__intro .handwrite{color:var(--blue);margin-bottom:16px}
.flap__badges{left:30px;top:500px;display:flex;gap:16px}
.badge{width:54px;height:40px;border-radius:6px;background:#e6d6e6}
.badge:nth-child(2){background:#d9ecd5;border-radius:50%;width:44px}
.badge:nth-child(3){background:#f3e2c7}
.flap__footer{left:0;top:690px;width:100%;height:116px;background:var(--purple);color:#fff;text-align:center}
.flap__tagline{font-family:"Fredoka",sans-serif;font-weight:600;font-size:19px;padding-top:8px}
.flap__contact{font-size:13px;line-height:1.4}
.social{left:0;top:776px;width:100%;height:30px;background:var(--green);display:flex;justify-content:space-around;align-items:center;color:#fff;font-size:11px;font-weight:700}
.social span{display:flex;align-items:center;gap:6px}
.social i{width:16px;height:16px;border-radius:50%;background:#fff;display:inline-block}

/* back panel */
.back{background:var(--green)}
.back__body{left:0;top:210px;width:100%;text-align:center;color:#fff}
.back__title{font-family:"Fredoka",sans-serif;font-weight:600;font-size:22px;line-height:1.2;padding:0 28px;margin-bottom:12px}
.back__list{font-size:15px;line-height:1.45;font-weight:700;margin:10px 0 16px}
.enrol{left:40px;top:590px;width:118px;height:118px;border-radius:50%;background:var(--blue);border:5px solid #fff;color:#fff;font-family:"Fredoka",sans-serif;font-weight:600;font-size:24px;line-height:1;display:flex;align-items:center;justify-content:center;text-align:center;z-index:2}
.back__footer{left:0;top:700px;width:100%;height:106px;background:var(--purple)}

/* cover panel */
.cover__brand{left:0;top:34px;width:100%;text-align:center}
.brand-mark{display:inline-flex;align-items:center;gap:10px}
.brand-dot{width:34px;height:34px;border-radius:50%;background:var(--green)}
.brand-name{font-family:"Fredoka",sans-serif;font-weight:600;font-size:46px;color:var(--purple);line-height:1}
.cover__sub{font-family:"Fredoka",sans-serif;font-weight:500;font-size:17px;color:var(--green-dark);margin-top:6px}
.star{position:absolute;width:92px;height:92px}
.cover__band{left:0;top:620px;width:100%;height:186px;background:var(--purple);color:#fff;text-align:center}
.cover__promise{font-family:"Fredoka",sans-serif;font-weight:600;font-size:20px;line-height:1.2;padding:26px 26px 14px}
.web-pill{display:inline-block;background:var(--green);color:#fff;font-weight:800;font-size:16px;padding:7px 30px;border-radius:22px}

/* inside left */
.story{background:var(--purple)}
.story__text{left:28px;top:30px;width:324px;color:#fff}
.story__text .handwrite{color:#fff;margin-bottom:16px}
.story__text .body-copy{color:#f2e6f2}

/* inside wide */
.learn__green{left:0;top:300px;width:100%;height:506px;background:var(--green)}
.learn__cols{left:30px;top:300px;width:700px;display:flex;gap:40px;color:#fff}
.learn__col{flex:1}
.quote{font-weight:800;font-size:12.5px;line-height:1.45;margin-bottom:10px;padding-left:26px;position:relative}
.quote::before{content:"\201C";position:absolute;left:0;top:-8px;font-family:"Fredoka",sans-serif;font-size:34px;color:#fff}
.learn__col .body-copy{color:#eef8ec}
.belief{background:rgba(255,255,255,.18);border-radius:10px;padding:12px 14px;font-weight:800;font-size:13px;line-height:1.4;margin-top:8px}
.learn__foot{left:0;top:776px;width:100%;height:30px;background:var(--purple)}
.circle-photo{position:absolute;border-radius:50%;border:5px solid #fff}
</style>
</head>
<body>

<!-- OUTSIDE SPREAD -->
<section class="spread spread--outside">

  <article class="panel flap">
    <div class="abs flap__intro">
      <h2 class="handwrite">Out of little things<br>big things grow!</h2>
      <p class="body-copy">We are a family-owned early learning centre offering long day care and a kindergarten program for children aged six weeks to six years.</p>
      <p class="body-copy">Our educators follow a play-based curriculum guided by the national framework, supporting each child's growth, wellbeing and sense of belonging.</p>
      <p class="body-copy">Learning happens indoors and outdoors, where children explore, create and build confidence through hands-on discovery every day.</p>
      <p class="body-copy">We also welcome school-age children for before and after school care and vacation programs.</p>
    </div>
    <div class="abs flap__badges"><span class="badge"></span><span class="badge"></span><span class="badge"></span></div>
    <div class="photo photo--yard" style="top:556px;height:150px" role="img" aria-label="Photo of the shaded outdoor play yard with sandpit and timber seating"></div>
    <svg class="curve" style="top:546px" width="380" height="30" viewBox="0 0 380 30" aria-hidden="true"><path d="M0 0H380V6Q190 34 0 14Z" fill="#fff"/><path d="M0 14Q190 34 380 6V10Q190 38 0 18Z" fill="#56b447"/></svg>
    <div class="abs flap__footer">
      <svg class="curve" style="top:-18px" width="380" height="22" viewBox="0 0 380 22" aria-hidden="true"><path d="M0 22V10Q190 -6 380 10V22Z" fill="#8e2a8b"/></svg>
      <p class="flap__tagline">Guiding the stewards of the future</p>
      <p class="flap__contact">hello@brightsprouts.example<br>08 5550 1234<br>brightsprouts.example</p>
    </div>
    <div class="abs social"><span><i></i>@brightsproutsec</span><span><i></i>@brightsproutsec</span></div>
  </article>

  <article class="panel back">
    <div class="photo photo--play" style="top:0;height:200px" role="img" aria-label="Photo of children playing together at an outdoor table"></div>
    <svg class="curve" style="top:176px" width="380" height="30" viewBox="0 0 380 30" aria-hidden="true"><path d="M0 30V12Q190 -8 380 16V30Z" fill="#56b447"/><path d="M0 12Q190 -8 380 16V10Q190 -14 0 6Z" fill="#fff"/></svg>
    <div class="abs back__body">
      <h2 class="back__title">Bright Sprouts Early Development &amp; Education Centre</h2>
      <span class="pill">We offer</span>
      <p class="back__list">Long day care (ages 6 weeks to 6 years)<br>Before and after school care (ages 6-12)<br>Vacation care (ages 6-12)<br>Adhoc casual bookings available</p>
      <span class="pill">Opening Hours</span>
      <p class="back__list">6:00am – 6:00pm Monday – Friday<br>(except public holidays)</p>
    </div>
    <div class="abs enrol">ENROL<br>NOW</div>
    <div class="abs back__footer"></div>
    <svg class="curve" style="top:680px" width="380" height="30" viewBox="0 0 380 30" aria-hidden="true"><path d="M0 30V16Q190 -6 380 14V30Z" fill="#8e2a8b"/></svg>
  </article>

  <article class="panel cover">
    <div class="abs cover__brand">
      <div class="brand-mark"><span class="brand-dot"></span><span class="brand-name">Bright Sprouts</span></div>
      <p class="cover__sub">Early Development &amp; Education Centre</p>
    </div>
    <div class="photo photo--warm" style="top:150px;height:490px" role="img" aria-label="Photo of children in sun hats playing on a rocky garden path"></div>
    <svg class="curve" style="top:140px" width="380" height="30" viewBox="0 0 380 30" aria-hidden="true"><path d="M0 0H380V8Q190 36 0 12Z" fill="#fff"/></svg>
    <svg class="star" style="left:262px;top:360px" viewBox="0 0 100 100" aria-hidden="true"><polygon points="50,4 62,36 96,38 69,59 79,93 50,73 21,93 31,59 4,38 38,36" fill="#fff" stroke="#2f9ad6" stroke-width="3"/></svg>
    <svg class="star" style="left:176px;top:430px" viewBox="0 0 100 100" aria-hidden="true"><polygon points="50,4 62,36 96,38 69,59 79,93 50,73 21,93 31,59 4,38 38,36" fill="#fff" stroke="#2f9ad6" stroke-width="3"/></svg>
    <svg class="star" style="left:272px;top:480px" viewBox="0 0 100 100" aria-hidden="true"><polygon points="50,4 62,36 96,38 69,59 79,93 50,73 21,93 31,59 4,38 38,36" fill="#fff" stroke="#2f9ad6" stroke-width="3"/></svg>
    <div class="abs cover__band">
      <p class="cover__promise">Proud provider of high quality childcare, education and learning outcomes for children</p>
      <span class="web-pill">brightsprouts.example</span>
    </div>
    <svg class="curve" style="top:596px" width="380" height="34" viewBox="0 0 380 34" aria-hidden="true"><path d="M0 34V20Q190 -6 380 18V34Z" fill="#8e2a8b"/><path d="M0 20Q190 -6 380 18V12Q190 -12 0 14Z" fill="#56b447"/></svg>
  </article>
</section>

<!-- INSIDE SPREAD -->
<section class="spread spread--inside">

  <article class="panel story">
    <div class="abs story__text">
      <h2 class="handwrite">Out of little things<br>big things grow!</h2>
      <p class="body-copy">Our children spend their days exploring spacious natural playgrounds with sandpits, gardens, climbing areas and quiet shaded corners to rest and reflect.</p>
      <p class="body-copy">Through play, children learn to share, solve problems and communicate, building the social skills they need for school and life.</p>
      <p class="body-copy">We value our partnership with families and keep parents informed through daily updates, regular meetings and a welcoming open-door approach.</p>
    </div>
    <div class="photo photo--child" style="top:470px;height:336px" role="img" aria-label="Photo of a young child in a sun hat playing in the garden"></div>
    <svg class="curve" style="top:456px" width="380" height="40" viewBox="0 0 380 40" aria-hidden="true"><path d="M0 0H380V10Q190 44 0 18Z" fill="#8e2a8b"/><path d="M0 18Q190 44 380 10V16Q190 50 0 24Z" fill="#56b447"/></svg>
    <svg class="curve" style="top:770px" width="380" height="36" viewBox="0 0 380 36" aria-hidden="true"><path d="M0 36V18Q190 0 380 14V36Z" fill="#56b447"/></svg>
  </article>

  <article class="panel panel--wide learn">
    <div class="photo photo--play" style="top:0;height:300px" role="img" aria-label="Photo of children at craft play wearing purple sun hats"></div>
    <div class="circle-photo photo--yard" style="left:470px;top:60px;width:110px;height:110px" role="img" aria-label="Round photo of outdoor play equipment"></div>
    <div class="circle-photo photo--warm" style="left:600px;top:40px;width:120px;height:120px" role="img" aria-label="Round photo of the garden play area"></div>
    <div class="abs learn__green"></div>
    <svg class="curve" style="top:250px" width="760" height="70" viewBox="0 0 760 70" aria-hidden="true"><path d="M0 70V40Q380 -10 760 30V70Z" fill="#56b447"/><path d="M0 40Q380 -10 760 30V22Q380 -18 0 32Z" fill="#fff"/></svg>
    <div class="abs learn__cols" style="top:320px">
      <div class="learn__col">
        <p class="quote">Outdoor play gives children space to move, imagine and connect with nature in a safe setting.</p>
        <p class="body-copy">Our educators plan experiences around each child's interests, helping them grow curious, capable and confident learners.</p>
        <p class="quote">Children who play freely learn to take safe risks and trust their own abilities.</p>
        <p class="body-copy">Natural materials such as sand, water, wood and plants invite open-ended play and creative thinking.</p>
        <p class="belief">We believe every child deserves a caring, inspiring place to learn and grow.</p>
      </div>
      <div class="learn__col">
        <p class="quote">Healthy meals, rest and routine help children feel settled, secure and ready to learn.</p>
        <p class="body-copy">From babies to school age, our rooms are designed to match each stage of development with age-appropriate resources.</p>
        <p class="quote">Strong relationships with educators give children the confidence to explore.</p>
        <p class="body-copy">Book a tour today to see our centre in action and meet our friendly, qualified team.</p>
      </div>
    </div>
    <div class="abs learn__foot"></div>
  </article>
</section>

</body>
</html>
```